Sole trader needs a stationery design

We are a sole trader competing in government and tertiary education tenders. We require stationery design to appear more professional than our previous Microsoft standard template.

Our new logo is attached.

Please feel free to add and adjust colours.

Please provide detail on the fonts you are using.

The uploaded font is Tex Gyre Adventor. It is the font of the logo.

Company Details:
Quillon IT

My details are as follows:
Name: Benedict Sallowmere
Role: Front end web consultant
Work: 02 8143 2296
Mobile: 0418 552 306
Address: not required
Email: bsallow@mailvane.net
Website: http://www.quillonit-demo.com.au

Target Market(s)

Government and tertiary institutions

Industry/Entity Type

Information Technology

Font styles to use
Sans Serif

Requirements
Must have
• We require the following stationery design:
• - Business cards
• - Physical letterhead
• - Tender document with coverpage and appendix coverpage
• - Internal tender page
• Content copy items to include:
• - Table
• - Image with caption (figure)
• - Figure text
• - Table of contents
• - Headings (up to 5 levels)
• - Paragraph with bold / italic text
• - Hyperlink
• - Ordered list
• - Bullet list
Should not have
• Serif fonts

```html
<!DOCTYPE html>
<html lang="en">
<head>
<meta charset="utf-8">
<title>Quillon IT Stationery</title>
<link rel="stylesheet" href="https://fonts.googleapis.com/css2?family=Jost:wght@400;500;600&display=swap">
<style>
  :root {
    --brand-blue: #3cc3f2;
    --brand-blue-deep: #1fa9e0;
    --brand-tint: #e6f7fd;
    --ink: #2b2b2b;
    --ink-soft: #555555;
    --paper: #ffffff;
    --backdrop: #e9ebec;
  }
  * { box-sizing: border-box; margin: 0; padding: 0; }
  html, body { width: 1200px; height: 1013px; overflow: hidden; }
  body {
    background: var(--backdrop);
    font-family: "Jost", sans-serif;
    color: var(--ink);
    position: relative;
  }

  /* Letterhead sheets */
  .letterhead {
    position: absolute;
    background: var(--paper);
    box-shadow: 0 2px 10px rgba(0,0,0,.14);
    overflow: hidden;
  }
  .letterhead--back { left: 165px; top: 250px; width: 555px; height: 668px; }
  .letterhead--front { left: 100px; top: 108px; width: 530px; height: 680px; }
  .letterhead__corner {
    position: absolute; top: 0; right: 0;
    width: 190px; height: 120px;
    background: var(--brand-tint);
    clip-path: polygon(30% 0, 100% 0, 100% 100%);
  }
  .brand {
    position: absolute; left: 54px; top: 54px;
    display: flex; align-items: center; gap: 8px;
  }
  .brand__mark { width: 24px; height: 24px; background: var(--brand-blue); }
  .brand__name { font-size: 34px; font-weight: 500; color: var(--brand-blue-deep); line-height: 1; }
  .sender { position: absolute; right: 58px; top: 58px; text-align: right; }
  .sender__name { font-size: 13px; font-weight: 600; color: var(--brand-blue); line-height: 1.1; }
  .sender__role { font-size: 6.5px; font-weight: 600; letter-spacing: .3px; text-transform: uppercase; }
  .recipient {
    position: absolute; right: 68px; top: 104px; text-align: right;
    font-size: 10.5px; line-height: 1.1;
  }
  .recipient__to { color: var(--brand-blue); }
  .recipient__name { font-weight: 600; }
  .letter-body {
    position: absolute; left: 63px; width: 410px; top: 214px;
    font-size: 9.6px; line-height: 13.6px; text-align: justify;
  }
  .letter-body p { margin-bottom: 13px; }
  .letter-body .salutation { font-weight: 600; margin-bottom: 0; }
  .signoff { margin-top: 26px; text-align: left; }
  .signoff__close { font-weight: 600; }
  .signature {
    display: block; width: 95px; height: 22px; margin-top: 10px;
    background: linear-gradient(90deg, #d6d6d6, #efefef);
  }
  .letterhead__footer {
    position: absolute; left: 0; right: 0; bottom: 0; height: 72px;
    background: var(--brand-blue);
    clip-path: polygon(0 40%, 100% 0, 100% 100%, 0 100%);
    display: flex; align-items: flex-end; gap: 8px;
    padding: 0 0 24px 36px;
    color: #fff; font-size: 8.5px; white-space: nowrap;
  }
  .footer-arrow { width: 9px; height: 8px; flex: none; align-self: center; margin-top: 14px; }

  /* Business cards */
  .card {
    position: absolute; width: 285px; height: 165px;
    box-shadow: 0 2px 8px rgba(0,0,0,.14); overflow: hidden;
  }
  .card--front { left: 805px; top: 112px; background: var(--paper); }
  .card--back { left: 805px; top: 385px; background: var(--brand-blue); }
  .card__tri-top {
    position: absolute; left: 0; top: 0; width: 120px; height: 36px;
    background: var(--brand-blue); clip-path: polygon(0 0, 100% 0, 0 100%);
  }
  .card__tri-left {
    position: absolute; left: 0; bottom: 0; width: 34px; height: 62px;
    background: var(--brand-blue); clip-path: polygon(0 0, 100% 100%, 0 100%);
  }
  .card__tri-bottom {
    position: absolute; right: 0; bottom: 0; width: 150px; height: 78px;
    background: var(--brand-blue); clip-path: polygon(100% 0, 100% 100%, 0 100%);
  }
  .card .brand { left: auto; right: 22px; top: 24px; gap: 5px; }
  .card .brand__mark { width: 14px; height: 14px; }
  .card .brand__name { font-size: 20px; }
  .card__person { position: absolute; left: 34px; top: 70px; }
  .card__name { font-size: 11px; font-weight: 600; color: var(--brand-blue); line-height: 1.1; }
  .card__role { font-size: 5.5px; font-weight: 600; text-transform: uppercase; }
  .card__contacts {
    position: absolute; left: 34px; top: 102px; list-style: none;
    font-size: 6.3px; line-height: 1.4; color: var(--ink-soft);
  }
  .card__contacts li { display: flex; gap: 6px; align-items: center; }
  .card__contacts .bullet { width: 4px; height: 4px; background: var(--ink); transform: rotate(45deg); }
  .card__contacts .label { width: 26px; color: var(--brand-blue); }
  .card--back .brand { right: 36px; top: auto; bottom: 40px; }
  .card--back .brand__mark { background: #fff; }
  .card--back .brand__name { color: #fff; }
</style>
</head>
<body>

  <article class="letterhead letterhead--back">
    <div class="letterhead__corner"></div>
    <div class="sender">
      <div class="sender__name">Benedict Sallowmere</div>
      <div class="sender__role">Front end web consultant</div>
    </div>
    <div class="recipient">
      <div class="recipient__to">TO:</div>
      <div class="recipient__name">Prof. Harlow,</div>
      <div>Mathematics Search Committee</div>
      <div>Department of Mathematics</div>
      <div>Westmere University</div>
      <div>Carrow Vale, Westmere 12345</div>
    </div>
    <div class="letter-body">
      <p class="salutation">Dear Sir or Madam,</p>
      <p>Lorem ipsum dolor sit amet, consectetur adipiscing elit. Praesent a nisi diam. Morbi consequat facilisis mi, sit amet laoreet velit aliquet quis. Sed a nisi vel augue ultricies blandit. Phasellus et congue dolor, at cursus dui. Integer quis faucibus metus. Vestibulum lobortis ligula in lectus pretium, in placerat lacus iaculis. Mauris nibh erat, condimentum at tortor at, sagittis viverra tortor.</p>
      <p>Pellentesque hendrerit neque quis quam fringilla, vitae vulputate quam bibendum. Fusce in hendrerit mauris. Mauris pretium libero eget convallis mattis. Vivamus nec nisi imperdiet, lacinia diam id, facilisis nulla. Vivamus eleifend augue ut libero tincidunt commodo. Vivamus sodales in lacus vitae dictum.</p>
      <p>Proin nunc erat, vestibulum quis tincidunt sit amet, cursus et libero. Aliquam erat volutpat. Sed vel malesuada velit. Vivamus risus arcu, facilisis non mauris sed, interdum varius tellus.</p>
    </div>
    <footer class="letterhead__footer">
      <svg class="footer-arrow" viewBox="0 0 9 8"><path d="M0 0l4 4-4 4M5 0l4 4-4 4" fill="none" stroke="#fff" stroke-width="1.3"/></svg>
      <span>Work: 02 8143 2296</span><span>|</span>
      <span>Mobile: 0418 552 306</span><span>|</span>
      <span>Email: bsallow@mailvane.net</span><span>|</span>
      <span>www.quillonit-demo.com.au</span>
    </footer>
  </article>

  <article class="letterhead letterhead--front">
    <div class="letterhead__corner"></div>
    <div class="brand">
      <span class="brand__mark"></span>
      <span class="brand__name">Quillon IT</span>
    </div>
    <div class="sender">
      <div class="sender__name">Benedict Sallowmere</div>
      <div class="sender__role">Front end web consultant</div>
    </div>
    <div class="recipient">
      <div class="recipient__to">TO:</div>
      <div class="recipient__name">Prof. Harlow,</div>
      <div>Mathematics Search Committee</div>
      <div>Department of Mathematics</div>
      <div>Westmere University</div>
      <div>Carrow Vale, Westmere 12345</div>
    </div>
    <div class="letter-body">
      <p class="salutation">Dear Sir or Madam,</p>
      <p>Lorem ipsum dolor sit amet, consectetur adipiscing elit. Praesent a nisi diam. Morbi consequat facilisis mi, sit amet laoreet velit aliquet quis. Sed a nisi vel augue ultricies blandit. Phasellus et congue dolor, at cursus dui. Integer quis faucibus metus. Vestibulum lobortis ligula in lectus pretium, in placerat lacus iaculis. Mauris nibh erat, condimentum at tortor at, sagittis viverra tortor. Vivamus posuere fermentum eros, rhoncus sagittis nisi imperdiet ac.</p>
      <p>Pellentesque hendrerit neque quis quam fringilla, vitae vulputate quam bibendum. Fusce in hendrerit mauris. Mauris pretium libero eget convallis mattis. Vivamus nec nisi imperdiet, lacinia diam id, facilisis nulla. Vivamus eleifend augue ut libero tincidunt commodo. Vivamus sodales in lacus vitae dictum. Nam et semper felis. Integer scelerisque accumsan condimentum. Aliquam laoreet erat vitae ornare consequat. Donec enim lacus, rutrum ut dui a, pretium mattis dui. Vivamus vulputate arcu nec congue convallis. Suspendisse faucibus turpis ac neque gravida, vel aliquet mauris tristique. In auctor fringilla nunc, sit amet tristique diam semper ac. Cras egestas nisi eu turpis facilisis, ac scelerisque elit lacinia. Sed eget adipiscing enim. Ut pulvinar ultrices purus ac eleifend.</p>
      <p>Proin nunc erat, vestibulum quis tincidunt sit amet, cursus et libero. Aliquam erat volutpat. Sed vel malesuada velit. Vivamus risus arcu, facilisis non mauris sed, interdum varius tellus. Vivamus aliquam vel sapien quis ultricies. Mauris venenatis risus enim, in dapibus quam volutpat in. Vivamus iaculis sapien sit amet massa vehicula, tempus facilisis nulla adipiscing. Mauris ullamcorper pharetra libero, quis sodales dolor blandit et. Donec convallis risus id euismod pharetra. Suspendisse placerat laoreet imperdiet. Praesent malesuada fringilla urna, non sollicitudin erat. Nullam arcu neque, lobortis nec facilisis at, scelerisque ac erat. Nunc quis tincidunt lorem, vitae laoreet enim.</p>
      <div class="signoff">
        <div class="signoff__close">Sincerely,</div>
        <div>Benedict Sallowmere</div>
        <div>Front end web consultant</div>
        <span class="signature" role="img" aria-label="Handwritten signature"></span>
      </div>
    </div>
    <footer class="letterhead__footer">
      <svg class="footer-arrow" viewBox="0 0 9 8"><path d="M0 0l4 4-4 4M5 0l4 4-4 4" fill="none" stroke="#fff" stroke-width="1.3"/></svg>
      <span>Work: 02 8143 2296</span><span>|</span>
      <span>Mobile: 0418 552 306</span><span>|</span>
      <span>Email: bsallow@mailvane.net</span><span>|</span>
      <span>www.quillonit-demo.com.au</span>
    </footer>
  </article>

  <article class="card card--front">
    <div class="card__tri-top"></div>
    <div class="card__tri-left"></div>
    <div class="card__tri-bottom"></div>
    <div class="brand">
      <span class="brand__mark"></span>
      <span class="brand__name">Quillon IT</span>
    </div>
    <div class="card__person">
      <div class="card__name">Benedict Sallowmere</div>
      <div class="card__role">Front end web consultant</div>
    </div>
    <ul class="card__contacts">
      <li><span class="bullet"></span><span class="label">Work:</span>02 8143 2296</li>
      <li><span class="bullet"></span><span class="label">Mobile:</span>0418 552 306</li>
      <li><span class="bullet"></span><span class="label">Email:</span>bsallow@mailvane.net</li>
      <li><span class="bullet"></span><span class="label">Web:</span>www.quillonit-demo.com.au</li>
    </ul>
  </article>

  <article class="card card--back">
    <div class="brand">
      <span class="brand__mark"></span>
      <span class="brand__name">Quillon IT</span>
    </div>
  </article>

</body>
</html>
```